Children's martial arts flyer for new classes

Need a postcard flyer addressing the attached spec (see file).

Flyer needs to be Postcard Size and be suited in style to the target demographic which is parents of children aged 5-12 years old.

Classes are new.

Postcard must include the logo and a picture. I have included an example pic in the attached file, but feel free to use other suitable pics.

Target Market(s)

Parents with children aged 5-12 years old

Colors

Designer to choose colors to be used in the design.

Requirements
Must have
• clean look.
• professional.

```html
<!DOCTYPE html>
<html lang="en">
<head>
<meta charset="utf-8">
<title>Children's Martial Art Classes Flyer</title>
<link href="https://fonts.googleapis.com/css2?family=Oswald:wght@500;600;700&family=Montserrat:wght@400;700;800&display=swap" rel="stylesheet">
<style>
  :root {
    --backdrop: #2a0508;
    --red-deep: #7a0c0c;
    --red: #c4160f;
    --red-bright: #e8321c;
    --glow: #ffe3dc;
    --gold: #f5a623;
    --white: #ffffff;
    --ink: #141414;
    --ring: #2b2b2b;
  }
  * { box-sizing: border-box; margin: 0; padding: 0; }
  html, body { width: 1200px; height: 1000px; overflow: hidden; }
  body {
    background: var(--backdrop);
    font-family: "Montserrat", Arial, sans-serif;
    position: relative;
  }
  .flyer {
    position: absolute;
    left: 290px; top: 60px;
    width: 620px; height: 880px;
    overflow: hidden;
    background:
      radial-gradient(ellipse 360px 420px at 220px 280px, var(--glow) 0%, #f7a08e 30%, rgba(232,50,28,0) 70%),
      radial-gradient(ellipse 300px 260px at 470px 230px, rgba(255,220,210,.75) 0%, rgba(232,50,28,0) 70%),
      linear-gradient(160deg, var(--red-bright) 0%, var(--red) 45%, var(--red-deep) 100%);
    box-shadow: 0 30px 60px rgba(0,0,0,.55);
  }
  .hero-photo {
    position: absolute; left: 50px; top: 40px;
    width: 225px; height: 530px;
    border-radius: 112px 112px 30px 30px;
    background: linear-gradient(180deg, #f4efe9 0%, #e6ddd3 60%, rgba(230,221,211,.15) 100%);
  }
  .brand {
    position: absolute; left: 370px; top: 110px; width: 220px;
    text-align: center; color: var(--white);
    font-family: "Oswald", Arial, sans-serif; font-weight: 600;
  }
  .brand-mark {
    width: 100px; height: 100px; border-radius: 50%;
    background: var(--gold); margin: 0 auto 12px;
  }
  .brand-name { font-size: 22px; line-height: 1.1; letter-spacing: .5px; }
  .brand-sub { font-size: 18px; letter-spacing: 8px; margin-top: 2px; }
  .class-photo {
    position: absolute; border-radius: 50%;
    border: 10px solid var(--ring);
    box-shadow: 0 0 0 3px #555, 0 6px 14px rgba(0,0,0,.5);
    background: radial-gradient(circle at 50% 40%, #ffffff 0%, #e9e9e9 70%, #cfcfcf 100%);
  }
  .class-photo--sparring { left: 292px; top: 410px; width: 165px; height: 165px; }
  .class-photo--stance { left: 422px; top: 355px; width: 110px; height: 110px; }
  .class-photo--floor { left: 432px; top: 440px; width: 140px; height: 140px; }
  .map {
    position: absolute; left: 30px; top: 590px;
    width: 250px; height: 145px;
    border: 3px solid var(--ink);
    background: linear-gradient(135deg, #eef0ea 0%, #e3e6de 55%, #cfe2c4 100%);
  }
  .address {
    position: absolute; left: 30px; top: 748px;
    color: var(--white); font-weight: 800; font-size: 13px;
    line-height: 1.3; text-transform: uppercase;
  }
  .divider {
    position: absolute; left: 300px; top: 612px;
    width: 2px; height: 178px; background: var(--white);
  }
  .headline {
    position: absolute; left: 318px; top: 610px;
    font-family: "Oswald", Arial, sans-serif; font-weight: 700;
    text-transform: uppercase; line-height: 1;
  }
  .headline-top { display: block; color: var(--gold); font-size: 46px; }
  .headline-main { display: block; color: var(--white); font-size: 30px; }
  .details {
    position: absolute; left: 318px; top: 704px;
    color: var(--white); font-size: 12px; line-height: 1.3;
    text-transform: uppercase;
  }
  .details strong { font-weight: 800; display: block; }
  .details span { display: block; font-weight: 400; }
  .details .schedule { margin-top: 6px; }
  .footer-bar {
    position: absolute; left: 0; bottom: 0;
    width: 100%; height: 66px; background: var(--ink);
    display: flex; align-items: center; justify-content: space-between;
    padding: 0 28px;
  }
  .call { color: var(--gold); font-weight: 700; font-size: 17px; }
  .call b { color: var(--white); font-weight: 800; }
  .social {
    display: flex; align-items: center; gap: 8px;
    color: var(--white); font-weight: 800; font-size: 13px;
  }
  .social-square { width: 16px; height: 16px; background: var(--gold); border-radius: 2px; }
</style>
</head>
<body>
  <main class="flyer">
    <div class="hero-photo" role="img" aria-label="Photo of a young student in a white uniform performing a high side kick"></div>

    <div class="brand">
      <div class="brand-mark"></div>
      <div class="brand-name">SUMMIT TAE KWON-DO</div>
      <div class="brand-sub">ACADEMY</div>
    </div>

    <div class="class-photo class-photo--sparring" role="img" aria-label="Photo of two students sparring in uniforms"></div>
    <div class="class-photo class-photo--stance" role="img" aria-label="Photo of a girl with a yellow belt in a ready stance"></div>
    <div class="class-photo class-photo--floor" role="img" aria-label="Photo of a child practising a technique on the mat"></div>

    <div class="map" role="img" aria-label="Street map showing the dojo location with a pin"></div>
    <p class="address">4/18 Larchmont Road<br>Kelvale VIC 3990</p>

    <div class="divider"></div>

    <h1 class="headline">
      <span class="headline-top">Children's</span>
      <span class="headline-main">Martial Art Classes</span>
    </h1>

    <div class="details">
      <strong>Fun and exciting yet</strong>
      <span>Controlled and disciplined</span>
      <strong class="schedule">Tuesday's and Thursday's</strong>
      <span>6PM</span>
    </div>

    <footer class="footer-bar">
      <p class="call">Call <b>0491 570 218</b> to book a free trial class</p>
      <div class="social"><span class="social-square"></span>STKDACAD</div>
    </footer>
  </main>
</body>
</html>
```